Nolvik Imaging Center web design and code

We need a new website for a Diagnostic Imaging Center in Fort Lauderdale, Florida.
The center has new RO advanced diagnostic equipment including a 3.0 Tesla MRI, a 128 slice PET/CT and a Varen T4 Ultrasound. Our facility has just been renovated and we have a lot of images, both facility and modality to use.
We have two client types, doctors who send their patients to our clinical Nolvik Center division, and clients who self-refer for screening studies to our Wellspire division. Both logos are attached. Please use the colors in the logos for the layout. Site should be coded in conventional HTML with CSS, but support multiple devices.
Updates

Reason: Waiting for additional designs. Most of the current designs are very similar in their structure and we would like more variety in terms of layout.

Target Market(s)

Doctors who refer patients for MRI, CT, PET, Bone Density and Ultrasound scans,
and
Retail clients who want full-body screening using MRI.

Industry/Entity Type

Medical Imaging

Coding

Coded - Design and coding required

Number of Pages Required

5+ page

Font styles to use
Sans Serif
Other font styles liked:
• Arquitecta

Requirements
Must have
• A good balance between color, shape, message and people/machine images.
• Must have images of the various machines, (RO Quillmark TN480, RO Quillmark 370, RO Varen T4) happy patients, clinical people, facility images and information about scans, preparations, costs, insurances we take.
• Must have links for social media and dynamic imagery.
Nice to have
• Some interactivity would be nice, including contact forms and scheduling application, Location map, directions, downloadable forms, history.
Should not have
• We do not want this to be built on WordPress platform. Should not be bound to a database platform that is proprietary or difficult to move.

```html
<!DOCTYPE html>
<html lang="en">
<head>
<meta charset="utf-8">
<title>Nolvik Imaging Center</title>
<link href="https://fonts.googleapis.com/css2?family=Open+Sans:wght@400;600;700&display=swap" rel="stylesheet">
<style>
:root{
  --green:#8cc63f;
  --green-dark:#6fa52a;
  --teal:#1f6f5c;
  --ink:#333;
  --muted:#666;
  --charcoal:#3b3b3b;
  --footer:#2e2e2e;
  --line:#d9d9d9;
  --paper:#fff;
}
*{box-sizing:border-box;margin:0;padding:0}
html,body{width:828px;height:1200px;overflow:hidden;background:var(--paper)}
body{font-family:"Open Sans",Arial,sans-serif;color:var(--ink);font-size:9px;line-height:1.5}
.wrap{width:760px;margin:0 auto;position:relative}

/* header */
.site-header{height:60px}
.site-header .wrap{display:flex;align-items:center;height:60px}
.brand{display:flex;align-items:center;gap:8px;width:250px}
.brand-dot{width:30px;height:30px;border-radius:50%;background:var(--green)}
.brand-name{font-size:15px;font-weight:700;color:var(--teal);line-height:1.05;text-transform:uppercase}
.main-nav{display:flex;gap:4px;margin-left:auto;align-items:center}
.main-nav a{font-size:10px;color:var(--muted);text-decoration:none;padding:5px 9px}
.main-nav a.active{background:var(--green);color:#fff}
.phone{display:flex;align-items:center;gap:5px;margin-left:14px;color:var(--green-dark);font-size:12px;font-weight:600}

/* hero */
.hero{height:290px;position:relative;background:linear-gradient(120deg,#bfc6c9,#e9eced 45%,#a9b2b6)}
.hero-caption{position:absolute;left:34px;top:150px;width:330px}
.hero-title{background:rgba(40,40,40,.8);color:#fff;font-size:19px;font-weight:700;padding:6px 12px;text-transform:uppercase}
.hero-text{background:rgba(111,165,42,.92);color:#fff;font-size:11px;padding:7px 12px;line-height:1.4}

/* welcome + schedule */
.intro{height:210px;padding-top:22px}
.intro .wrap{display:flex;gap:30px}
.welcome{flex:1}
.welcome h1{font-size:17px;font-weight:600;color:var(--ink);line-height:1.2}
.welcome h1 span{color:var(--teal);display:block}
.welcome p{margin:10px 0 12px;color:var(--muted)}
.btn{display:inline-block;background:var(--green);color:#fff;font-size:8px;font-weight:700;padding:6px 12px;text-transform:uppercase}
.schedule{width:250px;border:1px solid var(--line)}
.schedule h2{background:var(--charcoal);color:#fff;font-size:14px;font-weight:600;padding:5px 10px}
.schedule form{padding:10px}
.field{height:17px;border:1px solid var(--line);margin-bottom:6px;font-size:8px;color:#999;padding:2px 6px}
.field.tall{height:34px}
.schedule .btn{float:right}

/* about */
.about{height:200px;display:flex}
.about-text{width:50%;background:var(--green);color:#fff;padding:16px 20px 0 34px}
.about-text h2{font-size:16px;font-weight:600;line-height:1.2}
.about-text h3{font-size:10px;font-weight:600;margin-bottom:8px}
.about-text p{font-size:8px;margin-bottom:4px}
.about-side{width:50%;padding:16px 34px 0 24px}
.about-side .brand-name{font-size:16px}
.about-side .intro-line{margin:10px 0 6px;color:var(--muted);font-size:8px}
.checklist{list-style:none}
.checklist li{display:flex;align-items:center;gap:6px;font-size:8px;color:var(--muted);margin-bottom:3px}

/* wellspire */
.wellspire{height:140px;display:flex;background:var(--charcoal);color:#fff}
.wellspire-mark{width:260px;background:#fff;display:flex;align-items:center;justify-content:center;gap:8px;border-top:1px solid var(--line);border-bottom:1px solid var(--line)}
.wellspire-mark .sq{width:18px;height:18px;background:var(--green)}
.wellspire-mark span{font-size:26px;color:var(--muted);font-weight:400}
.wellspire-text{flex:1;padding:18px 34px 0 24px}
.wellspire-text h2{font-size:15px;font-weight:600}
.wellspire-text h3{font-size:10px;font-weight:600;margin-bottom:6px}
.wellspire-text p{font-size:8px;color:#ddd}

/* services */
.services{height:185px;padding-top:18px}
.services .wrap{display:flex;gap:30px}
.service{flex:1;display:flex;gap:12px}
.service-photo{width:130px;height:100px;flex:none}
.photo-exam{background:linear-gradient(135deg,#cfe0b0,#8fae6b)}
.photo-ins{background:linear-gradient(135deg,#e6e2da,#a9a49a)}
.service h2{font-size:15px;font-weight:600;color:var(--green-dark)}
.service p{font-size:8px;color:var(--muted);margin:4px 0 8px}

/* footer */
.site-footer{height:115px;background:var(--footer);color:#bbb;padding-top:20px}
.footer-row{display:flex;align-items:center}
.footer-nav{display:flex;gap:16px}
.footer-nav a{color:#ddd;text-decoration:none;font-size:9px}
.social{margin-left:auto;display:flex;gap:6px}
.social span{width:20px;height:20px;border-radius:50%;background:#4a6fa5}
.social span:nth-child(2){background:#4aa3df}
.social span:nth-child(3){background:#3c7bbf}
.social span:nth-child(4){background:#c94b3b}
.copyright{margin-top:14px;font-size:8px;border-top:1px solid #444;padding-top:10px}
</style>
</head>
<body>

<header class="site-header">
  <div class="wrap">
    <div class="brand"><span class="brand-dot"></span><span class="brand-name">Nolvik Imaging<br>Center</span></div>
    <nav class="main-nav">
      <a class="active" href="#">Home</a><a href="#">About</a><a href="#">Exams</a><a href="#">Wellspire</a><a href="#">Insurance</a><a href="#">Schedule</a><a href="#">Contact</a>
    </nav>
    <div class="phone">
      <svg width="14" height="14" viewBox="0 0 24 24"><circle cx="12" cy="12" r="12" fill="#8cc63f"/><path d="M8 6l2 3-1.5 1.5c.8 1.8 2.2 3.2 4 4L14 13l3 2-1 2.5c-4.5-.3-9-4.8-9.3-9.3z" fill="#fff"/></svg>
      954-555-0142
    </div>
  </div>
</header>

<section class="hero" role="img" aria-label="Bright scan room with an MRI machine and patient table">
  <div class="hero-caption">
    <div class="hero-title">Nolvik Imaging Center</div>
    <div class="hero-text">The center has new RO advanced diagnostic equipment including a 3.0 Tesla MRI, a 128 slice PET/CT and a Varen T4 Ultrasound</div>
  </div>
</section>

<section class="intro">
  <div class="wrap">
    <div class="welcome">
      <h1>Welcome to Our<span>MRI Diagnostic Imaging Center</span></h1>
      <p>Our renovated facility offers a calm and modern space for every patient. We provide MRI, CT, PET, bone density and ultrasound exams with fast results for referring doctors. Our caring staff guide you through each step, from booking to the final report, so you always know what to expect. Same week appointments are often available and most major insurance plans are accepted at our center.</p>
      <a class="btn" href="#">Read more</a>
    </div>
    <aside class="schedule">
      <h2>Schedule</h2>
      <form>
        <div class="field">Name</div>
        <div class="field">Email address</div>
        <div class="field">Phone number</div>
        <div class="field tall">Message</div>
        <a class="btn" href="#">Submit</a>
      </form>
    </aside>
  </div>
</section>

<section class="about">
  <div class="about-text">
    <h2>About Nolvik Center</h2>
    <h3>Why would you send your patients anywhere else?</h3>
    <p>Our radiologists read every study quickly and share clear reports with your office.</p>
    <p>Patients enjoy short waits, comfortable rooms and friendly, trained staff.</p>
    <p>We use the latest low dose methods to keep every scan safe.</p>
    <p>Online ordering and image access make referrals simple for doctors.</p>
    <p>We accept most plans and help patients with prior approvals.</p>
  </div>
  <div class="about-side">
    <div class="brand"><span class="brand-dot"></span><span class="brand-name">Nolvik Imaging<br>Center</span></div>
    <p class="intro-line">We proudly offer the most advanced RO diagnostic imaging systems including:</p>
    <ul class="checklist">
      <li><svg width="9" height="9" viewBox="0 0 10 10"><path d="M1 5l3 3 5-7" stroke="#8cc63f" stroke-width="2" fill="none"/></svg>3.0 Tesla MRI RO Quillmark TN480</li>
      <li><svg width="9" height="9" viewBox="0 0 10 10"><path d="M1 5l3 3 5-7" stroke="#8cc63f" stroke-width="2" fill="none"/></svg>128 slice PET/CT RO Quillmark 370</li>
      <li><svg width="9" height="9" viewBox="0 0 10 10"><path d="M1 5l3 3 5-7" stroke="#8cc63f" stroke-width="2" fill="none"/></svg>High resolution RO Varen T4 ultrasound</li>
      <li><svg width="9" height="9" viewBox="0 0 10 10"><path d="M1 5l3 3 5-7" stroke="#8cc63f" stroke-width="2" fill="none"/></svg>Bone density scanning</li>
    </ul>
  </div>
</section>

<section class="wellspire">
  <div class="wellspire-mark"><span class="sq"></span><span>Wellspire</span></div>
  <div class="wellspire-text">
    <h2>Wellspire</h2>
    <h3>Why wait until you are sick to find out about a serious health problem?</h3>
    <p>A full body MRI screening can find hidden issues early, when they are easiest to treat. No referral is needed and there is no radiation involved. Book your own scan, relax in a private suite and review your results with our physician in a personal follow up visit.</p>
  </div>
</section>

<section class="services">
  <div class="wrap">
    <article class="service">
      <div class="service-photo photo-exam" role="img" aria-label="Radiologist reviewing scan images"></div>
      <div>
        <h2>Exams</h2>
        <p>Learn how to prepare for your MRI, CT, PET, ultrasound or bone density exam and what happens on the day of your visit.</p>
        <a class="btn" href="#">Read more</a>
      </div>
    </article>
    <article class="service">
      <div class="service-photo photo-ins" role="img" aria-label="Insurance forms with a calculator"></div>
      <div>
        <h2>Insurance</h2>
        <p>We accept most major plans and Medicare. See our list of carriers and clear self pay prices for every exam.</p>
        <a class="btn" href="#">Read more</a>
      </div>
    </article>
  </div>
</section>

<footer class="site-footer">
  <div class="wrap">
    <div class="footer-row">
      <nav class="footer-nav"><a href="#">Home</a><a href="#">About</a><a href="#">Exams</a><a href="#">Wellspire</a><a href="#">Insurance</a><a href="#">Schedule</a><a href="#">Contact</a></nav>
      <div class="social"><span></span><span></span><span></span><span></span></div>
    </div>
    <p class="copyright">Copyright © 2024 Nolvik Imaging Center. All rights reserved.</p>
  </div>
</footer>

</body>
</html>
```